Harborline Crest Insurance Services

we are a high end insurance agency we specialize on Auto | Home | Business | Life looking for something professional and luxuries at the same time. if you guys need anything else please let me know.

Auto | Home | Business | Life must be under logo on the back with black background.

i want the back part to be black with our gold logo on it.

Target Market(s)

Auto | Home | Business | Life

Industry/Entity Type

Insurance Broker

Contact Information for Business Card

My logo is gold so a black in the back would be nice.

Font styles to use
Serif

Colors
000000

Requirements
Must have
• Big logo on the back with black background.

```html
<!DOCTYPE html>
<html lang="en">
<head>
<meta charset="utf-8">
<title>Harborline Crest Insurance Services – Business Card</title>
<link href="https://fonts.googleapis.com/css2?family=Libre+Baskerville&family=Arimo:wght@400&display=swap" rel="stylesheet">
<style>
  :root {
    --stage: #2a2a2a;
    --card-black: #000000;
    --card-white: #ffffff;
    --gold: #e0b21c;
    --gold-deep: #c9970e;
    --ink: #1f1f1f;
    --grey: #8e8e8e;
    --grey-light: #a8a8a8;
  }
  * { margin: 0; padding: 0; box-sizing: border-box; }
  html, body { width: 1200px; height: 900px; overflow: hidden; }
  body {
    background: var(--stage);
    position: relative;
    font-family: "Arimo", Arial, sans-serif;
  }
  .card {
    position: absolute;
    width: 700px;
    height: 400px;
  }
  /* Back side */
  .card-back {
    left: 90px; top: 70px;
    background: var(--card-black);
  }
  .back-brand {
    position: absolute;
    left: 56px; top: 250px;
    display: flex; align-items: center; gap: 12px;
  }
  .brand-dot {
    width: 14px; height: 14px; border-radius: 50%;
    background: var(--gold);
    flex: none;
  }
  .brand-name {
    font-family: "Libre Baskerville", Georgia, serif;
    font-weight: 400;
    color: var(--gold);
    white-space: nowrap;
  }
  .back-brand .brand-name { font-size: 24px; letter-spacing: 0.3px; }
  .service-line {
    position: absolute;
    left: 82px; top: 298px;
    font-size: 15px;
    letter-spacing: 0.8px;
    color: var(--gold);
  }
  .service-line .sep { color: #ffffff; margin: 0 6px; }
  .accent-rule {
    position: absolute;
    left: 330px; right: 0; top: 232px;
    height: 1.5px;
    background: var(--gold-deep);
  }
  /* Front side */
  .card-front {
    left: 410px; top: 430px;
    background: var(--card-white);
    box-shadow: 0 4px 18px rgba(0,0,0,0.45);
  }
  .front-brand {
    position: absolute;
    left: 56px; top: 170px;
    display: flex; align-items: center; gap: 10px;
  }
  .front-brand .brand-name { font-size: 19px; }
  .holder {
    position: absolute;
    left: 440px; top: 56px;
  }
  .holder-name {
    font-family: "Libre Baskerville", Georgia, serif;
    font-size: 17px;
    letter-spacing: 0.5px;
    color: var(--ink);
  }
  .holder-role {
    margin-top: 4px;
    font-size: 14px;
    color: var(--grey-light);
  }
  .contact-list {
    position: absolute;
    left: 450px; top: 222px;
    list-style: none;
  }
  .contact-list li {
    display: flex; align-items: center; gap: 12px;
    font-size: 15px;
    color: var(--ink);
    height: 27px;
  }
  .contact-list svg { width: 13px; height: 13px; flex: none; }
  .address {
    position: absolute;
    left: 56px; bottom: 40px;
    font-size: 16px;
    color: var(--grey-light);
  }
</style>
</head>
<body>

  <section class="card card-back" aria-label="Card back">
    <div class="back-brand">
      <span class="brand-dot"></span>
      <span class="brand-name">Harborline Crest Insurance Services</span>
    </div>
    <p class="service-line">AUTO<span class="sep">|</span>HOME<span class="sep">|</span>BUSINESS<span class="sep">|</span>LIFE</p>
    <div class="accent-rule"></div>
  </section>

  <section class="card card-front" aria-label="Card front">
    <div class="front-brand">
      <span class="brand-dot"></span>
      <span class="brand-name">Harborline Crest Insurance Services</span>
    </div>

    <div class="holder">
      <p class="holder-name">MAREN HOLLOWAY</p>
      <p class="holder-role">Managing Director</p>
    </div>

    <ul class="contact-list">
      <li>
        <svg viewBox="0 0 16 16" aria-hidden="true"><path d="M3 1.5l3 .5 1 3.5-2 1.3a9 9 0 0 0 4.2 4.2l1.3-2 3.5 1 .5 3c-.3.8-1.2 1.5-2.2 1.5C6.5 14.5 1.5 9.5 1.5 3.7c0-1 .7-1.9 1.5-2.2z" fill="var(--gold)"/></svg>
        +1 555-014-2287
      </li>
      <li>
        <svg viewBox="0 0 16 16" aria-hidden="true"><rect x="1.5" y="3.5" width="13" height="9" fill="none" stroke="var(--gold)" stroke-width="1.4"/><path d="M1.5 3.5L8 9l6.5-5.5" fill="none" stroke="var(--gold)" stroke-width="1.4"/></svg>
        info@harborlinecrest.com
      </li>
      <li>
        <svg viewBox="0 0 16 16" aria-hidden="true"><circle cx="8" cy="8" r="6.5" fill="none" stroke="var(--gold)" stroke-width="1.4"/><ellipse cx="8" cy="8" rx="2.8" ry="6.5" fill="none" stroke="var(--gold)" stroke-width="1.2"/><path d="M1.5 8h13" stroke="var(--gold)" stroke-width="1.2"/></svg>
        www.harborlinecrest.com
      </li>
    </ul>

    <p class="address">240 Linden Ave. Marlow Bay, CA 94012</p>
  </section>

</body>
</html>
```